Halvering & Partners, LLC Business Card 2016

We need a new business card design for a very important trade show coming up.

We are a compliance Consulting Firm. Our clients are stock brokerage firms and investment advisers.

I would like our logo on both sides of the card.

Info in the front of the card shold include:

Logo
First & Last Name
Title
Office #
Cell #
Email
Company Address (42 W. Calloway Blvd., Suite 300 Pasadena, CA 91847

Back of the card should include the logo and url: www.halveringpartnersgroup.com

Target Market(s)

Stock Brokerage Firms and Investment Advisers

Industry/Entity Type

Financial Service

Contact Information for Business Card

Russell K. Halvering
President
42 W. Calloway Blvd., Suite 300
Pasadena, CA 91847
O 626.555.0147 ext. 204
C 818.555.0192
Email: russ@halveringpartnersgroup.com
www.halveringpartnersgroup.com

Requirements
Nice to have
• The back of the card could be black with the logo with the white letters.
• I do want the front of the card to at least have the color logo with the black "Halvering & Partners Lettering.

```html
<!DOCTYPE html>
<html lang="en">
<head>
<meta charset="utf-8">
<title>Halvering &amp; Partners Business Card</title>
<link rel="stylesheet" href="https://fonts.googleapis.com/css2?family=Cinzel:wght@500;600&family=Montserrat:wght@400;500&display=swap">
<style>
  :root {
    --page: #e6e6e6;
    --ink: #050505;
    --paper: #ffffff;
    --red: #d8322a;
    --red-deep: #a91d17;
    --grey-text: #b9b9b9;
    --white: #ffffff;
  }
  * { box-sizing: border-box; margin: 0; padding: 0; }
  html, body { width: 1200px; height: 900px; overflow: hidden; }
  body {
    background: var(--page);
    font-family: "Montserrat", sans-serif;
    position: relative;
  }
  .card {
    position: absolute;
    width: 620px;
    height: 354px;
    border-radius: 26px;
    overflow: hidden;
    box-shadow: 0 6px 18px rgba(0,0,0,.22);
  }
  .card-back { left: 290px; top: 70px; background: var(--ink); }
  .card-front { left: 290px; top: 476px; background: var(--paper); }

  .wordmark {
    position: absolute;
    display: flex;
    align-items: center;
    gap: 16px;
  }
  .wordmark-square {
    width: 44px; height: 44px;
    background: var(--red);
  }
  .wordmark-name {
    font-family: "Cinzel", serif;
    font-weight: 600;
    font-size: 34px;
    letter-spacing: 1px;
    white-space: nowrap;
  }
  .card-back .wordmark { left: 70px; top: 128px; }
  .card-back .wordmark-name { color: var(--white); }
  .back-url {
    position: absolute;
    left: 0; right: 0; top: 262px;
    text-align: center;
    color: var(--white);
    font-size: 15px;
    font-weight: 500;
    letter-spacing: 2px;
  }

  .front-art { position: absolute; inset: 0; }
  .card-front .wordmark { left: 30px; top: 156px; gap: 10px; }
  .card-front .wordmark-square { width: 26px; height: 26px; }
  .card-front .wordmark-name { color: var(--ink); font-size: 21px; letter-spacing: .3px; }

  .contact {
    position: absolute;
    left: 398px; top: 50px;
    width: 204px;
    color: var(--white);
  }
  .contact-name {
    font-family: "Cinzel", serif;
    font-weight: 500;
    color: var(--red);
    font-size: 15px;
    line-height: 1.1;
    white-space: nowrap;
  }
  .contact-title {
    color: var(--grey-text);
    font-size: 10px;
    margin-top: 3px;
    margin-bottom: 14px;
  }
  .contact-list { list-style: none; }
  .contact-list li {
    display: flex;
    align-items: center;
    gap: 7px;
    font-size: 9.5px;
    font-weight: 500;
    line-height: 1;
    margin-bottom: 9px;
    white-space: nowrap;
  }
  .contact-list svg { width: 10px; height: 10px; flex: none; }
  .contact-address {
    font-size: 9.5px;
    font-weight: 500;
    line-height: 1.5;
    margin-top: 12px;
    white-space: nowrap;
  }
</style>
</head>
<body>

<section class="card card-back" aria-label="Card back">
  <div class="wordmark">
    <span class="wordmark-square"></span>
    <span class="wordmark-name">Halvering &amp; Partners</span>
  </div>
  <p class="back-url">www.halveringpartnersgroup.com</p>
</section>

<section class="card card-front" aria-label="Card front">
  <svg class="front-art" width="620" height="354" viewBox="0 0 620 354" aria-hidden="true">
    <defs>
      <linearGradient id="paperFade" x1="0" y1="0" x2="1" y2="1">
        <stop offset="0" stop-color="#ffffff"/>
        <stop offset="1" stop-color="#eef0f3"/>
      </linearGradient>
      <linearGradient id="bandFade" x1="0" y1="0" x2="0" y2="1">
        <stop offset="0" stop-color="#a91d17"/>
        <stop offset="1" stop-color="#d8322a"/>
      </linearGradient>
    </defs>
    <rect width="620" height="354" fill="url(#paperFade)"/>
    <path d="M250 0 Q390 120 390 354 L620 354 L620 0 Z" fill="#050505"/>
    <path d="M250 0 Q390 120 390 354 L362 354 Q370 150 250 0 Z" fill="url(#bandFade)"/>
  </svg>

  <div class="wordmark">
    <span class="wordmark-square"></span>
    <span class="wordmark-name">Halvering &amp; Partners</span>
  </div>

  <div class="contact">
    <p class="contact-name">Russell K. Halvering</p>
    <p class="contact-title">Managing Director</p>
    <ul class="contact-list">
      <li>
        <svg viewBox="0 0 12 12"><path d="M2.5 1 L4.5 1 L5.2 3.6 L4 4.6 Q5 6.9 7.4 8 L8.4 6.8 L11 7.5 L11 9.5 Q10.5 11 9 11 Q3 10.4 1 3 Q1 1.5 2.5 1 Z" fill="#d8322a"/></svg>
        626-555-0147
      </li>
      <li>
        <svg viewBox="0 0 12 12"><rect x="1" y="5" width="10" height="6" fill="#d8322a"/><rect x="3" y="1" width="6" height="4" fill="none" stroke="#d8322a" stroke-width="1.4"/></svg>
        626-555-0149
      </li>
      <li>
        <svg viewBox="0 0 12 12"><rect x="1" y="2.5" width="10" height="7.5" fill="none" stroke="#d8322a" stroke-width="1.4"/><path d="M1 3 L6 7 L11 3" fill="none" stroke="#d8322a" stroke-width="1.4"/></svg>
        info@halveringpartnersgroup.com
      </li>
      <li>
        <svg viewBox="0 0 12 12"><circle cx="6" cy="6" r="5" fill="none" stroke="#d8322a" stroke-width="1.4"/><path d="M1 6 H11 M6 1 Q3 6 6 11 M6 1 Q9 6 6 11" fill="none" stroke="#d8322a" stroke-width="1"/></svg>
        halveringpartnersgroup.com
      </li>
    </ul>
    <p class="contact-address">42 W. Calloway Blvd., Suite 300<br>Pasadena, CA 91847</p>
  </div>
</section>

</body>
</html>
```